Revamp of business card

i need to revamp my business card to look more modern and neat

Contact Information for Business Card

details provided in pdf file, text will change

```html
<!DOCTYPE html>
<html lang="en">
<head>
<meta charset="utf-8">
<title>Brightmark business card</title>
<link rel="stylesheet" href="https://fonts.googleapis.com/css2?family=Quicksand:wght@500;600;700&display=swap">
<style>
  :root {
    --stage: #8a8a8a;
    --paper: #ffffff;
    --brand-orange: #f15a24;
    --accent-red: #e8262b;
    --accent-blue: #1b4f9c;
    --accent-green: #1f9a46;
    --accent-amber: #f7941d;
    --ink: #3d3d3d;
    --rule: #555555;
    --soft-white: #fbd3c3;
  }
  * { box-sizing: border-box; margin: 0; padding: 0; }
  html, body {
    width: 1200px; height: 800px; overflow: hidden;
    background: var(--stage);
    font-family: "Quicksand", sans-serif;
  }
  .stage {
    width: 1200px; height: 800px;
    display: flex; align-items: center; justify-content: center; gap: 40px;
  }
  .card {
    position: relative;
    width: 560px; height: 320px;
    overflow: hidden;
    box-shadow: 0 10px 24px rgba(0,0,0,.25);
  }

  /* Front */
  .card-front { background: var(--paper); }
  .front-brand {
    position: absolute; left: 28px; top: 136px;
    display: flex; align-items: center; gap: 10px;
  }
  .brand-dot { width: 16px; height: 16px; border-radius: 50%; background: var(--accent-red); }
  .front-brand .brand-name {
    font-size: 36px; font-weight: 700; color: var(--brand-orange); letter-spacing: -0.5px;
  }
  .front-divider {
    position: absolute; left: 292px; top: 64px;
    width: 1px; height: 184px; background: var(--rule);
  }
  .contact {
    position: absolute; left: 312px; top: 70px; width: 240px;
    color: var(--ink);
  }
  .contact-name { font-size: 20px; font-weight: 700; color: var(--brand-orange); line-height: 1.1; }
  .contact-role { font-size: 12px; font-weight: 600; color: var(--accent-green); margin-bottom: 10px; }
  .contact-address { font-size: 12px; font-weight: 600; line-height: 1.4; margin-bottom: 8px; }
  .contact-list { list-style: none; font-size: 12px; font-weight: 600; line-height: 1.55; }
  .contact-list li { display: flex; align-items: center; gap: 7px; }
  .icon {
    width: 14px; height: 14px; border-radius: 50%;
    display: inline-flex; align-items: center; justify-content: center; flex: none;
  }
  .icon svg { width: 8px; height: 8px; }
  .icon-mobile { background: var(--accent-red); }
  .icon-phone { background: var(--accent-blue); }
  .icon-mail { background: var(--accent-green); }
  .icon-web { background: var(--accent-amber); }
  .colour-band {
    position: absolute; left: 0; bottom: 0; width: 100%; height: 8px;
    display: flex;
  }
  .colour-band span { flex: 1; }
  .band-red { background: var(--accent-red); }
  .band-blue { background: var(--accent-blue); }
  .band-green { background: var(--accent-green); }
  .band-amber { background: var(--accent-amber); }

  /* Back */
  .card-back { background: var(--brand-orange); color: var(--paper); }
  .services { position: absolute; left: 30px; top: 22px; width: 340px; }
  .service { margin-bottom: 8px; }
  .service-title { font-size: 16px; font-weight: 700; line-height: 1.2; }
  .service-detail { font-size: 11px; font-weight: 600; line-height: 1.3; }
  .service-links { font-size: 11px; font-weight: 600; line-height: 1.3; color: var(--soft-white); }
  .social { display: flex; gap: 14px; font-size: 11px; font-weight: 600; margin-top: 4px; }
  .social span { display: flex; align-items: center; gap: 5px; }
  .social-dot { width: 10px; height: 10px; border-radius: 50%; background: var(--paper); }
  .back-brand {
    position: absolute; right: 30px; top: 130px;
    display: flex; align-items: center; gap: 10px;
  }
  .back-brand .brand-dot { width: 22px; height: 22px; background: var(--accent-blue); }
  .back-brand .brand-name { font-size: 34px; font-weight: 700; color: var(--paper); letter-spacing: -0.5px; }
</style>
</head>
<body>
<main class="stage">

  <section class="card card-front" aria-label="Card front">
    <div class="front-brand">
      <span class="brand-dot"></span>
      <span class="brand-name">Brightmark</span>
    </div>
    <div class="front-divider"></div>
    <div class="contact">
      <p class="contact-name">Daniel Harwood</p>
      <p class="contact-role">Director</p>
      <p class="contact-address">Unit 4, 18 Harbour Lane,<br>Eastgate Arcade,<br>Millbrook 5100</p>
      <ul class="contact-list">
        <li><span class="icon icon-mobile"><svg viewBox="0 0 10 10"><path d="M2 1h2l1 2-1.2 1a5 5 0 0 0 2.2 2.2L7 5l2 1v2a1 1 0 0 1-1 1A7 7 0 0 1 1 2a1 1 0 0 1 1-1z" fill="#fff"/></svg></span>0400 000 123</li>
        <li><span class="icon icon-phone"><svg viewBox="0 0 10 10"><path d="M2 1h2l1 2-1.2 1a5 5 0 0 0 2.2 2.2L7 5l2 1v2a1 1 0 0 1-1 1A7 7 0 0 1 1 2a1 1 0 0 1 1-1z" fill="#fff"/></svg></span>08 7000 0199</li>
        <li><span class="icon icon-mail"><svg viewBox="0 0 10 10"><rect x="1" y="2" width="8" height="6" fill="#fff"/><path d="M1 2l4 3 4-3" stroke="#1f9a46" fill="none"/></svg></span>daniel@brightmark.example</li>
        <li><span class="icon icon-web"><svg viewBox="0 0 10 10"><circle cx="5" cy="5" r="3.6" fill="none" stroke="#fff" stroke-width="1.2"/><path d="M1.5 5h7M5 1.5v7" stroke="#fff"/></svg></span>www.brightmark.example</li>
      </ul>
    </div>
    <div class="colour-band">
      <span class="band-red"></span><span class="band-blue"></span><span class="band-green"></span><span class="band-amber"></span>
    </div>
  </section>

  <section class="card card-back" aria-label="Card back">
    <div class="services">
      <div class="service">
        <p class="service-title">Embroidery</p>
        <p class="service-detail">Logos stitched on apparel and fabrics</p>
        <p class="service-links">www.stitchworks.example<br>www.fullhue.example<br>www.threadline.example</p>
      </div>
      <div class="service">
        <p class="service-title">Prints on Promotional &amp; Giveaways</p>
        <p class="service-detail">Mugs, Caps KeyChains,Name Tags,Wall Clocks ets</p>
      </div>
      <div class="service">
        <p class="service-title">Print &amp; Design Services</p>
        <p class="service-detail">Business Cards, Flyers,<br>Brochures,Posters, Banners ets</p>
      </div>
      <div class="service">
        <p class="service-title">Photo Prints</p>
        <p class="service-detail">HD Metal Prints to Photographic Paper Prints</p>
      </div>
      <div class="social">
        <span><i class="social-dot"></i>brightmarkstudio</span>
        <span><i class="social-dot"></i>brightmark</span>
      </div>
    </div>
    <div class="back-brand">
      <span class="brand-dot"></span>
      <span class="brand-name">Brightmark</span>
    </div>
  </section>

</main>
</body>
</html>
```